Online Course Page

We are building a video based online course page. This project is for only the actual page that the student will watch the videos at. They will watch one vide at a time. Once one video lesson is completed then they can move to the next video lesson. The page will need to show the video player. (Main feature.) The list of lessons in the course. Instructor information. Profile picture and bio of the instructor. A Live chat button that will initiate a chat in real-time with the instructor.

The winning designer will also be asked to to design the dashboard area and other aspects of the user interface as an additional project.

Target Market(s)

Adults

Number of Pages Required

1 page

Colors
9bcb3c

Requirements
Must have
• Our logo is attached. Green and grey are our colors. Should feel modern, clean and be simple to navigate. The site will be responsive so the layout should work well on mobile devices.

```html
<!DOCTYPE html>
<html lang="en">
<head>
<meta charset="utf-8">
<title>CourseDock – How To Get Started</title>
<link href="https://fonts.googleapis.com/css2?family=Lato:wght@400;700&display=swap" rel="stylesheet">
<style>
:root{
  --green:#9bcb3c;
  --navy:#1f3a5c;
  --muted:#9aa7b8;
  --muted-dot:#c9ced6;
  --line:#e4e6ea;
  --page:#f7f7f7;
  --white:#ffffff;
  --text:#2b2b2b;
  --badge:#e0274a;
  --scroll:#d9d9d9;
}
*{box-sizing:border-box;margin:0;padding:0}
html,body{width:1200px;height:993px;overflow:hidden}
body{font-family:'Lato',sans-serif;background:var(--page);position:relative;color:var(--text)}
.site-header{position:absolute;left:0;top:0;width:1200px;height:74px;background:var(--white);border-bottom:1px solid var(--line)}
.brand{position:absolute;left:44px;top:24px;display:flex;align-items:center;gap:7px;font-size:17px;font-weight:700;color:var(--green)}
.brand-dot{width:16px;height:16px;border-radius:50%;background:var(--green)}
.user-avatar{position:absolute;left:1108px;top:17px;width:41px;height:41px;border-radius:50%;background:radial-gradient(circle at 50% 40%,#c99b7c,#7a5a44)}
.user-badge{position:absolute;left:1136px;top:15px;width:15px;height:15px;border-radius:50%;background:var(--badge);color:#fff;font-size:8px;font-weight:700;text-align:center;line-height:15px}
.lesson-nav{position:absolute;left:0;top:75px;width:329px;height:918px;background:var(--white)}
.scrollbar{position:absolute;left:329px;top:75px;width:9px;height:918px;background:#f1f1f1}
.scrollbar span{position:absolute;left:0;top:15px;width:9px;height:93px;background:var(--scroll)}
.module{position:absolute;left:40px;width:270px}
.module h2{font-size:18px;font-weight:400;color:var(--navy);display:flex;align-items:center;gap:10px;height:22px}
.module h2 svg{width:11px;height:8px}
.module ul{list-style:none;margin-top:22px}
.module li{display:flex;justify-content:space-between;align-items:center;height:38.8px;font-size:14.5px;color:var(--muted)}
.module li .title{display:flex;align-items:center;gap:7px}
.module li .title::before{content:"";width:5px;height:5px;border-radius:50%;background:var(--muted-dot)}
.module li .len{font-size:7.5px;color:var(--muted);margin-right:6px}
.player{position:absolute;left:386px;top:110px;width:764px;height:421px;background:#1b1a18;overflow:hidden}
.player-media{position:absolute;inset:0;background:linear-gradient(135deg,#3a2d22 0%,#7a5a3c 28%,#33424a 50%,#2c2a24 72%,#4a3a2a 100%)}
.player-title{position:absolute;left:45px;top:18px;font-size:19px;color:#fff}
.play-btn{position:absolute;left:359px;top:183px;width:44px;height:44px;border-radius:50%;background:rgba(40,40,40,.8)}
.progress{position:absolute;left:0;top:378px;width:764px;height:3px;background:#e8e8e8}
.progress .buffer{position:absolute;left:0;top:0;width:160px;height:3px;background:#7fa863}
.progress .done{position:absolute;left:0;top:0;width:105px;height:3px;background:var(--green)}
.controls{position:absolute;left:0;top:381px;width:764px;height:40px;background:#0d0d0d;color:#fff}
.controls svg{position:absolute}
.time{position:absolute;left:137px;top:14px;font-size:7.5px}
.instructor-card{position:absolute;left:386px;top:562px;width:765px;height:371px;background:var(--white);border:1px solid #ececec;box-shadow:0 1px 3px rgba(0,0,0,.06)}
.instructor-photo{position:absolute;left:22px;top:21px;width:106px;height:84px;background:linear-gradient(135deg,#4c5a3e,#b88a6a 55%,#3d4633)}
.instructor-name{position:absolute;left:22px;top:117px;font-size:14px;font-weight:700;color:#1a1a1a}
.social{position:absolute;left:44px;top:143px;display:flex;gap:8px}
.social span{width:8px;height:8px;border-radius:50%;background:#1a1a1a}
.bio{position:absolute;left:150px;top:22px;width:590px;font-size:14.5px;line-height:25px;color:#222}
.bio p+p{margin-top:25px}
</style>
</head>
<body>
<header class="site-header">
  <div class="brand"><span class="brand-dot"></span>CourseDock</div>
  <div class="user-avatar" role="img" aria-label="Student profile photo"></div>
  <div class="user-badge">1</div>
</header>

<nav class="lesson-nav">
  <section class="module" style="top:37px">
    <h2><svg viewBox="0 0 11 8"><path d="M1 1.5l4.5 4.5 4.5-4.5" fill="none" stroke="#1f3a5c" stroke-width="2.2"/></svg>1 . Introduction</h2>
    <ul>
      <li><span class="title">nunc mattis enim ut</span><span class="len">11 min</span></li>
      <li><span class="title">nunc mattis enim ut</span><span class="len">11 min</span></li>
      <li><span class="title">nunc mattis enim ut</span><span class="len">11 min</span></li>
      <li><span class="title">nunc mattis enim ut</span><span class="len">11 min</span></li>
      <li><span class="title">nunc mattis enim ut</span><span class="len">11 min</span></li>
    </ul>
  </section>
  <section class="module" style="top:306px">
    <h2><svg viewBox="0 0 11 8"><path d="M1 1.5l4.5 4.5 4.5-4.5" fill="none" stroke="#1f3a5c" stroke-width="2.2"/></svg>2 . Getting Started</h2>
    <ul>
      <li><span class="title">nunc mattis enim ut</span><span class="len">11 min</span></li>
      <li><span class="title">nunc mattis enim ut</span><span class="len">11 min</span></li>
      <li><span class="title">nunc mattis enim ut</span><span class="len">11 min</span></li>
      <li><span class="title">nunc mattis enim ut</span><span class="len">11 min</span></li>
      <li><span class="title">nunc mattis enim ut</span><span class="len">11 min</span></li>
    </ul>
  </section>
  <section class="module" style="top:575px">
    <h2><svg viewBox="0 0 11 8"><path d="M1 1.5l4.5 4.5 4.5-4.5" fill="none" stroke="#1f3a5c" stroke-width="2.2"/></svg>3 . First Lesson</h2>
    <ul>
      <li><span class="title">nunc mattis enim ut</span><span class="len">11 min</span></li>
      <li><span class="title">nunc mattis enim ut</span><span class="len">11 min</span></li>
      <li><span class="title">nunc mattis enim ut</span><span class="len">11 min</span></li>
      <li><span class="title">nunc mattis enim ut</span><span class="len">11 min</span></li>
      <li><span class="title">nunc mattis enim ut</span><span class="len">11 min</span></li>
    </ul>
  </section>
</nav>
<div class="scrollbar"><span></span></div>

<main>
  <div class="player">
    <div class="player-media" role="img" aria-label="Video frame: laptop showing a photo editing app on a desk with a lamp and a plant"></div>
    <div class="player-title">How To Get Started</div>
    <div class="play-btn"><svg width="44" height="44" viewBox="0 0 44 44"><path d="M18 14l12 8-12 8z" fill="#fff"/></svg></div>
    <div class="progress"><span class="buffer"></span><span class="done"></span></div>
    <div class="controls">
      <svg style="left:45px;top:12px" width="12" height="16" viewBox="0 0 12 16"><rect x="0" y="0" width="4" height="16" fill="#fff"/><rect x="8" y="0" width="4" height="16" fill="#fff"/></svg>
      <svg style="left:74px;top:14px" width="11" height="11" viewBox="0 0 11 11"><path d="M0 0l8 5.5-8 5.5z" fill="#fff"/><rect x="8.5" y="0" width="2.5" height="11" fill="#fff"/></svg>
      <svg style="left:100px;top:14px" width="12" height="11" viewBox="0 0 12 11"><path d="M0 3.5h3l4-3.5v11l-4-3.5h-3z" fill="#fff"/><path d="M9 3.5q1.5 2 0 4" stroke="#fff" fill="none"/></svg>
      <span class="time">2:24 / 11:15</span>
      <svg style="left:671px;top:12px" width="16" height="16" viewBox="0 0 16 16"><circle cx="8" cy="8" r="5" fill="none" stroke="#fff" stroke-width="3" stroke-dasharray="2.6 1.3"/><circle cx="8" cy="8" r="4" fill="#fff"/><circle cx="8" cy="8" r="1.8" fill="#0d0d0d"/></svg>
      <svg style="left:706px;top:12px" width="15" height="15" viewBox="0 0 15 15"><path d="M1 5V1h4M10 1h4v4M14 10v4h-4M5 14H1v-4" fill="none" stroke="#fff" stroke-width="2"/></svg>
    </div>
  </div>

  <section class="instructor-card">
    <div class="instructor-photo" role="img" aria-label="Instructor portrait photo"></div>
    <div class="instructor-name">Instructor Name</div>
    <div class="social"><span></span><span></span><span></span><span></span></div>
    <div class="bio">
      <p>Lorem ipsum dolor sit amet, consectetur adipiscing elit, sed do eiusmod tempor incididunt ut labore et dolore magna aliqua. Lorem ipsum dolor sit amet, consectetur adipiscing elit, sed do eiusmod tempor incididunt ut labore et dolore magna aliqua.</p>
      <p>Lorem ipsum dolor sit amet, consectetur adipiscing elit, sed do eiusmod tempor incididunt ut labore et dolore magna aliqua. Vestibulum sed arcu non odio euismod lacinia. Magna etiam tempor orci eu lobortis elementum nibh tellus molestie.</p>
      <p>Lorem ipsum dolor sit amet, consectetur adipiscing elit, sed do eiusmod tempor incididunt ut labore et dolore magna aliqua. Ut faucibus pulvinar elementum integer enim neque volutpat. Consectetur adipiscing elit pellentesque habitant morbi tristique. Ut porttitor leo a diam sollicitudin tempor. Sagittis id consectetur purus ut faucibus pulvinar elementum integer enim. Sit amet nisl purus in mollis nunc sed.</p>
    </div>
  </section>
</main>
</body>
</html>
```